Ongoing Practitioner Learning Sessions
Brochure Template
Ongoing Practitioner Learning Sessions - Law
Creative Brief
Law
Professional - Lawyers. OPLS provides legal training and education seminar for lawyers.
OPLS organises and presents regular legal professional seminars throughout Australia. Our marketing is heavily based on direct mail. When we schedule our seminars we design and print brochures and send them to all lawyers that are close to the location of the seminars. The brochures contain information that relates to the specific seminars that are scheduled. Therefore, the content is tailored specifically to the events that each brochure advertises. We currently use a brochure template that accommodates four individual seminars. We have used this template for the past couple of years and would like to update/improve the design. I will upload several PDF examples of the template we currently use, but do not feel constrained by this. We are looking for some imagination and new ideas. However, it will still need to have the following elements: 1. The brochure size needs to be as follows (note – this is the equivalent of a normal DL sized brochure but double size – instead of 3 panels, each side has 6) • Width – 599 mm • Height – 214 mm • Pages – two (front and back) • Panels – 12 (6 front and 6 back) 2. The front panel needs to have the following: • Our logo • The titles of each of the four events • The location and date of the seminars (Month/Year is sufficient) 3. The design of the balance of the brochure does not need to have any other specific requirements. However, it must contain the content to advertise each event as well as a registration form and the additional information that is contained in our existing brochures. I would not be too concerned with the actual content. The design for the front panel is the most important element. Also, we need a complementary graphical design/layout for the rest of the brochure. This includes a consistent layout, fonts and other graphical elements. One thing to keep in mind is that the layout should be simple. Complex or busy designs that have a lot of photos/graphics will not work. Also, I would probably prefer graphics or abstract designs to photos. The template will need to be supplied in a format that will allow the content to be edited using InDesign. Please note that we often schedule 8, 12 or 16 seminars at the same time. As each brochure advertises 4 seminars, we often will send out 2-4 different brochures in the same envelope. If all the brochures are exactly the same design, a casual receiver may assume that all the brochures are the same and only read one of the brochures and discard the others. Therefore, we need to be able to change the graphic or design on the front cover so that two or more brochures will instantly be recognised as different. We have always done this in the past by simply having a graphic on the front that we can change the colour. For example, we can have a blue version, a red version, a green version, etc. Last thing to note is that I also wish to redesign the icon set we use to designate the compulsory subject areas for our seminars. I will create a separate project for this, but you may wish to consider submitting a design for this as well. Please see this project for the specific details, but in short, we would like to redesign the icons that we use for the compulsory subjects. At the moment we use stock art, but we would like to use a custom designed icon set.

```html
<!DOCTYPE html>
<html lang="en">
<head>
<meta charset="utf-8">
<title>Ongoing Practitioner Learning Sessions – Brochure Template</title>
<link href="https://fonts.googleapis.com/css2?family=Open+Sans:wght@400;600;700&display=swap" rel="stylesheet">
<style>
  :root{
    --bg:#8e9093;
    --paper:#ffffff;
    --ink:#3a3a3a;
    --muted:#6f6f6f;
    --blue:#1f4f9c;
    --red:#d8262b;
    --label:#d9dadb;
  }
  *{box-sizing:border-box;margin:0;padding:0}
  html,body{width:1200px;height:923px;overflow:hidden}
  body{background:var(--bg);font-family:"Open Sans",Arial,sans-serif;color:var(--ink);position:relative}
  .brochure{position:absolute;left:10px;width:1155px;height:435px;background:var(--paper);
    display:grid;grid-template-columns:repeat(6,1fr);box-shadow:0 2px 6px rgba(0,0,0,.35)}
  .brochure--blue{top:8px;--accent:var(--blue)}
  .brochure--red{top:466px;--accent:var(--red)}
  .panel{position:relative;padding:12px 11px;border-right:1px solid #ececec;overflow:hidden}
  .panel:last-child{border-right:0}
  .copy{font-size:5.4px;line-height:1.5;color:var(--muted);margin-bottom:4px}
  .copy b{color:var(--ink);font-weight:700}
  .lead{font-size:5.6px;font-weight:700;color:var(--ink);margin-bottom:4px;line-height:1.4}
  .list{font-size:5.4px;line-height:1.5;color:var(--muted);padding-left:9px;margin-bottom:4px}
  .list ul{padding-left:8px}
  .title-block{position:absolute;left:0;right:0;bottom:30px;height:78px;background:var(--accent);color:#fff;padding:16px 12px 0}
  .title-block h2{font-size:10px;line-height:1.2;font-weight:700}
  .title-block p{font-size:5px;margin-top:4px;line-height:1.45}
  .section-bar{background:var(--accent);color:#fff;font-size:6.5px;font-weight:700;padding:4px 11px;margin:0 -11px 6px}
  .bar-low{margin-top:auto}
  .head-band{background:var(--accent);color:#fff;margin:6px -11px 8px;padding:7px 11px 8px}
  .head-band h3{font-size:8.5px;font-weight:700}
  .head-band p{font-size:4.8px;margin-top:2px}
  .subject{display:flex;align-items:center;gap:4px;font-size:5px;color:var(--muted);margin-bottom:4px;line-height:1.3}
  .subject i{width:10px;height:10px;background:var(--accent);display:block;flex:none}
  .subject b{color:var(--ink)}
  .footer-url{position:absolute;bottom:6px;right:11px;font-size:4.8px;color:var(--muted)}
  .swoosh{position:absolute;left:0;right:0;bottom:0;height:60px}
  .stack{display:flex;flex-direction:column;height:100%}
  .cover{padding:0}
  .cover-head{background:var(--red);color:#fff;font-size:6.8px;font-weight:700;padding:6px 10px;text-align:right}
  .venue{padding:12px 12px 0 90px;font-size:6.5px;line-height:1.35;color:var(--accent);border-bottom:1px solid #eee;padding-bottom:10px}
  .venue strong{font-size:9px;display:block}
  .wordmark{display:flex;align-items:center;justify-content:center;gap:5px;margin:36px auto 40px;font-size:16px;font-weight:700;color:var(--accent)}
  .wordmark .dot{width:12px;height:12px;border-radius:50%;background:var(--accent)}
  .events{list-style:none}
  .events li{background:var(--accent);color:#fff;font-size:6.2px;font-weight:700;padding:0 10px;margin-bottom:3px;line-height:1.3;height:28px;display:flex;align-items:center}
  .version{position:absolute;right:4px;width:30px;writing-mode:vertical-rl;transform:rotate(180deg);
    font-size:16px;color:var(--label);text-align:center}
  .version--blue{top:155px}
  .version--red{top:610px}
</style>
</head>
<body>

<section class="brochure brochure--blue" aria-label="Blue version">
  <div class="panel">
    <p class="lead">From the Trade Practices Act to the Competition &amp; Consumer Act</p>
    <p class="copy">The new Act took effect early this year and replaced the older trade regime with one national framework for fair dealing across every state and territory.</p>
    <p class="copy">This session reviews the main changes and what they mean for advice given to business and private clients in daily practice.</p>
    <p class="copy">It covers unfair contract terms, product safety rules, consumer guarantees and the penalty regime now in force, with examples drawn from recent matters.</p>
    <p class="copy">The regulator has been given wider powers to seek orders, issue notices and pursue civil penalties, so the risk profile for firms has changed.</p>
    <p class="copy">Practitioners will leave with a clear picture of the points to raise with clients and the documents most likely to need review.</p>
    <p class="copy">The session will address the following:</p>
    <ul class="list">
      <li>The key changes in outline</li>
      <li>The scope of the new law</li>
      <li>Unfair contract terms in standard form deals</li>
      <li>The new statutory guarantees, including:
        <ul><li>supply of goods and services</li><li>remedies for major failures</li></ul></li>
      <li>Enforcement and penalties</li>
      <li>Transitional issues for existing contracts</li>
    </ul>
    <div class="title-block">
      <h2>Role and Legal Liability of Non Executive Directors</h2>
      <p>Tuesday, 15 November 2011<br>2.30 pm – 5.30 pm</p>
    </div>
  </div>
  <div class="panel">
    <div class="stack">
      <ul class="list">
        <li>The current statutory considerations</li>
        <li>The duties owed to the company and members</li>
        <li>Recent cases on director conduct and reliance</li>
        <li>Insurance and indemnity arrangements</li>
      </ul>
      <div class="subject"><i></i><span><b>Compulsory Area 1</b> · Legal Ethics and Practice<br>Compulsory Area 3 · Substantive Law</span></div>
      <div class="section-bar bar-low">About the Presenter</div>
      <p class="copy">The presenter is a senior partner with many years in corporate and commercial work, advising listed and private boards on governance, disclosure and risk. She has acted in several major director liability cases and sits on two advisory committees.</p>
      <p class="copy">She speaks often at industry events, lectures in a postgraduate law program and writes on director duties for a number of journals.</p>
      <p class="copy" style="margin-bottom:26px">Her practical style and clear explanations make this session well suited to practitioners at every level of experience.</p>
    </div>
  </div>
  <div class="panel">
    <div class="head-band"><h3>The New Australian Consumer Law</h3><p>Thursday, 10 November 2011 · 2.30 pm – 5.30 pm</p></div>
    <p class="lead">From the Trade Practices Act to the Competition &amp; Consumer Act</p>
    <p class="copy">A practical guide to the national consumer law and its effect on daily legal work, from first client meeting to final advice.</p>
    <p class="copy">The new provisions now apply in all jurisdictions and replace the consumer protection parts of the former Act and the state fair trading laws.</p>
    <p class="copy">This session explains the structure of the law, the way courts have begun to read it, and the steps firms should take now.</p>
    <p class="copy">The session will address the following:</p>
    <ul class="list">
      <li>Background to the reforms</li>
      <li>Misleading and deceptive conduct</li>
      <li>Unconscionable conduct</li>
      <li>Unfair terms in consumer contracts</li>
      <li>Consumer guarantees and remedies</li>
      <li>Product safety and recalls</li>
      <li>Penalties and infringement notices</li>
    </ul>
    <div class="subject"><i></i><span><b>Compulsory Area 3</b> · Substantive Law<br>Three points</span></div>
    <svg class="swoosh" viewBox="0 0 192 60" preserveAspectRatio="none" aria-hidden="true"><path d="M0 58 L192 24" stroke="var(--accent)" stroke-width="1"/><path d="M0 60 L192 32" stroke="var(--accent)" stroke-width=".6"/></svg>
  </div>
  <div class="panel">
    <div class="section-bar">About the Presenter</div>
    <p class="copy">The presenter is a partner in a leading firm with long experience in litigation and regulatory matters. He has advised retailers, manufacturers and service providers on compliance and has acted in a number of contested cases brought by the regulator.</p>
    <p class="copy">He was part of a working group that gave input on the draft law and has since delivered training to in-house legal teams across the country.</p>
    <p class="copy">His work is regularly recognised in independent guides to the profession, and he is a frequent speaker at conferences.</p>
    <p class="copy">The session will also cover:</p>
    <ul class="list">
      <li>Current market practice</li>
      <li>Key regulator actions to date</li>
      <li>Drafting tips for standard contracts</li>
      <li>Handling complaints and refunds</li>
      <li>Advising small business clients</li>
    </ul>
    <div class="subject"><i></i><span><b>Compulsory Area 1</b> · Legal Ethics and Practice</span></div>
    <div class="subject"><i></i><span><b>Compulsory Area 2</b> · Practice Management</span></div>
    <svg class="swoosh" viewBox="0 0 192 60" preserveAspectRatio="none" aria-hidden="true"><path d="M0 24 L192 4" stroke="var(--accent)" stroke-width="1"/><path d="M0 32 L192 12" stroke="var(--accent)" stroke-width=".6"/></svg>
  </div>
  <div class="panel">
    <div class="section-bar" style="background:var(--red)">OPLS Information</div>
    <p class="copy"><b>Mandatory Continuing Education Points</b></p>
    <p class="copy">Each session earns three points toward the yearly requirement in the areas listed below.</p>
    <div class="subject"><i></i>Compulsory Area 1 · Legal Ethics and Practice</div>
    <div class="subject"><i></i>Compulsory Area 2 · Practice Management</div>
    <div class="subject"><i></i>Compulsory Area 3 · Substantive Law</div>
    <p class="copy">Practitioners should check their own records to confirm that they meet the yearly requirement in each area.</p>
    <p class="copy"><b>Registration</b></p>
    <p class="copy">Bookings close one week before each session. Fees include seminar notes, afternoon tea and a certificate of attendance. Payment must be received before the date.</p>
    <p class="copy"><b>Cancellations</b></p>
    <p class="copy">A substitute may attend at no cost. Refunds, less a small handling fee, apply up to seven days prior. No refunds after that time.</p>
    <p class="copy"><b>Program Changes</b></p>
    <p class="copy">We reserve the right to change a presenter or date if needed. Registrants will be told as early as possible.</p>
    <p class="copy"><b>Enquiries</b><br>Phone 08 5550 1420<br>Fax 08 5550 1421<br>Email info@opls.com.au</p>
    <span class="footer-url">www.opls.com.au</span>
  </div>
  <div class="panel cover">
    <div class="cover-head">OPLS Seminars November 2011</div>
    <div class="venue"><strong>Perth</strong>Harbourline Hotel<br>14 Cardinal Row</div>
    <div class="wordmark"><span class="dot"></span>OPLS</div>
    <ul class="events">
      <li>Personal Property Securities Update</li>
      <li>Aspects of Litigation for Discrete Corporations</li>
      <li>10 Most Common Drafting Myths</li>
      <li>Property Transactions and the Australian Consumer Law</li>
    </ul>
  </div>
</section>

<section class="brochure brochure--red" aria-label="Red version">
  <div class="panel">
    <p class="lead">From the Trade Practices Act to the Competition &amp; Consumer Act</p>
    <p class="copy">The new Act took effect early this year and replaced the older trade regime with one national framework for fair dealing across every state and territory.</p>
    <p class="copy">This session reviews the main changes and what they mean for advice given to business and private clients in daily practice.</p>
    <p class="copy">It covers unfair contract terms, product safety rules, consumer guarantees and the penalty regime now in force, with examples drawn from recent matters.</p>
    <p class="copy">The regulator has been given wider powers to seek orders, issue notices and pursue civil penalties, so the risk profile for firms has changed.</p>
    <p class="copy">Practitioners will leave with a clear picture of the points to raise with clients and the documents most likely to need review.</p>
    <p class="copy">The session will address the following:</p>
    <ul class="list">
      <li>The key changes in outline</li>
      <li>The scope of the new law</li>
      <li>Unfair contract terms in standard form deals</li>
      <li>The new statutory guarantees, including:
        <ul><li>supply of goods and services</li><li>remedies for major failures</li></ul></li>
      <li>Enforcement and penalties</li>
      <li>Transitional issues for existing contracts</li>
    </ul>
    <div class="title-block">
      <h2>Role and Legal Liability of Non Executive Directors</h2>
      <p>Tuesday, 15 November 2011<br>2.30 pm – 5.30 pm</p>
    </div>
  </div>
  <div class="panel">
    <div class="stack">
      <ul class="list">
        <li>The current statutory considerations</li>
        <li>The duties owed to the company and members</li>
        <li>Recent cases on director conduct and reliance</li>
        <li>Insurance and indemnity arrangements</li>
      </ul>
      <div class="subject"><i></i><span><b>Compulsory Area 1</b> · Legal Ethics and Practice<br>Compulsory Area 3 · Substantive Law</span></div>
      <div class="section-bar bar-low">About the Presenter</div>
      <p class="copy">The presenter is a senior partner with many years in corporate and commercial work, advising listed and private boards on governance, disclosure and risk. She has acted in several major director liability cases and sits on two advisory committees.</p>
      <p class="copy">She speaks often at industry events, lectures in a postgraduate law program and writes on director duties for a number of journals.</p>
      <p class="copy" style="margin-bottom:26px">Her practical style and clear explanations make this session well suited to practitioners at every level of experience.</p>
    </div>
  </div>
  <div class="panel">
    <div class="head-band"><h3>The New Australian Consumer Law</h3><p>Thursday, 10 November 2011 · 2.30 pm – 5.30 pm</p></div>
    <p class="lead">From the Trade Practices Act to the Competition &amp; Consumer Act</p>
    <p class="copy">A practical guide to the national consumer law and its effect on daily legal work, from first client meeting to final advice.</p>
    <p class="copy">The new provisions now apply in all jurisdictions and replace the consumer protection parts of the former Act and the state fair trading laws.</p>
    <p class="copy">This session explains the structure of the law, the way courts have begun to read it, and the steps firms should take now.</p>
    <p class="copy">The session will address the following:</p>
    <ul class="list">
      <li>Background to the reforms</li>
      <li>Misleading and deceptive conduct</li>
      <li>Unconscionable conduct</li>
      <li>Unfair terms in consumer contracts</li>
      <li>Consumer guarantees and remedies</li>
      <li>Product safety and recalls</li>
      <li>Penalties and infringement notices</li>
    </ul>
    <div class="subject"><i></i><span><b>Compulsory Area 3</b> · Substantive Law<br>Three points</span></div>
    <svg class="swoosh" viewBox="0 0 192 60" preserveAspectRatio="none" aria-hidden="true"><path d="M0 58 L192 24" stroke="var(--accent)" stroke-width="1"/><path d="M0 60 L192 32" stroke="var(--accent)" stroke-width=".6"/></svg>
  </div>
  <div class="panel">
    <div class="section-bar">About the Presenter</div>
    <p class="copy">The presenter is a partner in a leading firm with long experience in litigation and regulatory matters. He has advised retailers, manufacturers and service providers on compliance and has acted in a number of contested cases brought by the regulator.</p>
    <p class="copy">He was part of a working group that gave input on the draft law and has since delivered training to in-house legal teams across the country.</p>
    <p class="copy">His work is regularly recognised in independent guides to the profession, and he is a frequent speaker at conferences.</p>
    <p class="copy">The session will also cover:</p>
    <ul class="list">
      <li>Current market practice</li>
      <li>Key regulator actions to date</li>
      <li>Drafting tips for standard contracts</li>
      <li>Handling complaints and refunds</li>
      <li>Advising small business clients</li>
    </ul>
    <div class="subject"><i></i><span><b>Compulsory Area 1</b> · Legal Ethics and Practice</span></div>
    <div class="subject"><i></i><span><b>Compulsory Area 2</b> · Practice Management</span></div>
    <svg class="swoosh" viewBox="0 0 192 60" preserveAspectRatio="none" aria-hidden="true"><path d="M0 24 L192 4" stroke="var(--accent)" stroke-width="1"/><path d="M0 32 L192 12" stroke="var(--accent)" stroke-width=".6"/></svg>
  </div>
  <div class="panel">
    <div class="section-bar" style="background:var(--red)">OPLS Information</div>
    <p class="copy"><b>Mandatory Continuing Education Points</b></p>
    <p class="copy">Each session earns three points toward the yearly requirement in the areas listed below.</p>
    <div class="subject"><i></i>Compulsory Area 1 · Legal Ethics and Practice</div>
    <div class="subject"><i></i>Compulsory Area 2 · Practice Management</div>
    <div class="subject"><i></i>Compulsory Area 3 · Substantive Law</div>
    <p class="copy">Practitioners should check their own records to confirm that they meet the yearly requirement in each area.</p>
    <p class="copy"><b>Registration</b></p>
    <p class="copy">Bookings close one week before each session. Fees include seminar notes, afternoon tea and a certificate of attendance. Payment must be received before the date.</p>
    <p class="copy"><b>Cancellations</b></p>
    <p class="copy">A substitute may attend at no cost. Refunds, less a small handling fee, apply up to seven days prior. No refunds after that time.</p>
    <p class="copy"><b>Program Changes</b></p>
    <p class="copy">We reserve the right to change a presenter or date if needed. Registrants will be told as early as possible.</p>
    <p class="copy"><b>Enquiries</b><br>Phone 08 5550 1420<br>Fax 08 5550 1421<br>Email info@opls.com.au</p>
    <span class="footer-url">www.opls.com.au</span>
  </div>
  <div class="panel cover">
    <div class="cover-head">OPLS Seminars November 2011</div>
    <div class="venue"><strong>Perth</strong>Harbourline Hotel<br>14 Cardinal Row</div>
    <div class="wordmark"><span class="dot"></span>OPLS</div>
    <ul class="events">
      <li>Personal Property Securities Update</li>
      <li>Aspects of Litigation for Discrete Corporations</li>
      <li>10 Most Common Drafting Myths</li>
      <li>Property Transactions and the Australian Consumer Law</li>
    </ul>
  </div>
</section>

<div class="version version--blue">Blue Version</div>
<div class="version version--red">Red Version</div>

</body>
</html>
```